Bulk Food Container sticker

Our company sells bulk snacks to office locations. We re-package all sorts of foods into re-usable "Vessaline" type containers for consistency. We need to create a designed sticker which has room to laser-print the name of the food. The "blank" sticker needs to be designed with our logo, etc... I have attached 2 files. The first is an example from another company doing a similar work, and the second is the template from the company that will be printing the stickers for me. See our website for examples of our current corporate identity. www.brindlemoorbeans.com
Target Market(s)
Offices, tech companies
Industry/Entity Type
Printing
Look and feel

```html
<!DOCTYPE html>
<html lang="en">
<head>
<meta charset="utf-8">
<title>Brindlemoor Beans – Vessaline Container Stickers</title>
<link rel="stylesheet" href="https://fonts.googleapis.com/css2?family=Arimo:wght@400;700&display=swap">
<style>
  :root {
    --brown: #7f4a00;
    --orange: #e06b00;
    --white: #ffffff;
    --page: #ffffff;
  }
  html, body {
    margin: 0;
    padding: 0;
    width: 1200px;
    height: 1146px;
    overflow: hidden;
    background: var(--page);
  }
  .sheet {
    position: relative;
    width: 1058px;
    height: 1011px;
    transform: scale(1.1342);
    transform-origin: 0 0;
    font-family: "Arimo", Arial, sans-serif;
  }
  .sticker {
    position: absolute;
    width: 394px;
    height: 396px;
    border-radius: 10px;
    overflow: hidden;
  }
  .sticker--tagline { left: 77px;  top: 61px; }
  .sticker--tall    { left: 588px; top: 61px; }
  .sticker--framed  { left: 77px;  top: 555px; }
  .sticker--split   { left: 588px; top: 555px; }

  .sticker__ground {
    position: absolute;
    inset: 0;
    width: 100%;
    height: 100%;
  }
  .ground-brown  { fill: var(--brown); }
  .ground-orange { fill: var(--orange); }

  .print-area {
    position: absolute;
    left: 24px;
    width: 344px;
    background: var(--white);
    border-radius: 16px;
  }
  .sticker--tagline .print-area { top: 118px; height: 231px; }
  .sticker--tall .print-area    { top: 24px;  height: 325px; }
  .sticker--framed .print-area  { top: 26px;  height: 343px; }
  .sticker--split .print-area--brand { top: 24px;  height: 110px; border-radius: 10px; }
  .sticker--split .print-area--label { top: 153px; height: 193px; border-radius: 16px; }

  .brand-name {
    position: absolute;
    left: 0;
    right: 0;
    margin: 0;
    text-align: center;
    color: var(--brown);
    font-weight: 700;
    font-size: 33px;
    letter-spacing: -0.5px;
    line-height: 1;
  }
  .sticker--tagline .brand-name { bottom: 38px; }
  .sticker--tall .brand-name,
  .sticker--framed .brand-name { top: 44px; }
  .sticker--split .brand-name { top: 38px; }

  .headline {
    position: absolute;
    left: 55px;
    top: 28px;
    margin: 0;
    color: var(--white);
    font-weight: 700;
    font-size: 22.5px;
    line-height: 31px;
    letter-spacing: 0.4px;
  }
  .headline__sub {
    display: block;
    font-size: 12.5px;
    line-height: 12px;
    letter-spacing: 0.3px;
  }

  .web-address {
    position: absolute;
    left: 0;
    right: 0;
    margin: 0;
    text-align: center;
    font-weight: 700;
    font-size: 17px;
    letter-spacing: 0.3px;
    line-height: 1;
    color: var(--white);
    top: 362px;
  }
  .sticker--framed .web-address {
    color: var(--brown);
    top: 332px;
  }
</style>
</head>
<body>
<main class="sheet">

  <section class="sticker sticker--tagline">
    <svg class="sticker__ground" viewBox="0 0 394 396" preserveAspectRatio="none" aria-hidden="true">
      <rect class="ground-brown" width="394" height="396"/>
      <polygon class="ground-orange" points="394,57 394,396 0,396 0,331"/>
    </svg>
    <h2 class="headline">ENHANCING OFFICE<br>PRODUCTIVITY<span class="headline__sub">ONE TUB AT A TIME...</span></h2>
    <div class="print-area">
      <p class="brand-name">Brindlemoor Beans</p>
    </div>
    <p class="web-address">www.brindlemoorbeans.com</p>
  </section>

  <section class="sticker sticker--tall">
    <svg class="sticker__ground" viewBox="0 0 394 396" preserveAspectRatio="none" aria-hidden="true">
      <rect class="ground-brown" width="394" height="396"/>
      <polygon class="ground-orange" points="394,57 394,396 0,396 0,331"/>
    </svg>
    <div class="print-area">
      <p class="brand-name">Brindlemoor Beans</p>
    </div>
    <p class="web-address">www.brindlemoorbeans.com</p>
  </section>

  <section class="sticker sticker--framed">
    <svg class="sticker__ground" viewBox="0 0 394 396" preserveAspectRatio="none" aria-hidden="true">
      <rect class="ground-brown" width="394" height="396"/>
      <polygon class="ground-orange" points="394,57 394,396 0,396 0,331"/>
    </svg>
    <div class="print-area">
      <p class="brand-name">Brindlemoor Beans</p>
    </div>
    <p class="web-address">www.brindlemoorbeans.com</p>
  </section>

  <section class="sticker sticker--split">
    <svg class="sticker__ground" viewBox="0 0 394 396" preserveAspectRatio="none" aria-hidden="true">
      <rect class="ground-brown" width="394" height="396"/>
      <polygon class="ground-orange" points="394,57 394,396 0,396 0,331"/>
    </svg>
    <div class="print-area print-area--brand">
      <p class="brand-name">Brindlemoor Beans</p>
    </div>
    <div class="print-area print-area--label"></div>
    <p class="web-address">www.brindlemoorbeans.com</p>
  </section>

</main>
</body>
</html>
```